Simon Ashgrove Pianist Teacher Examiner

I need a website design to promote my business as a professional classical pianist and a piano teacher of all levels.
I want it to look a mixture of old world opulence (eg antique grand piano?) and modern text. It should have an elegant, beautiful and relaxing feel.

Industry/Entity Type

Teacher

```html
<!DOCTYPE html>
<html lang="en">
<head>
<meta charset="utf-8">
<title>Simon Ashgrove — Pianist Teacher Examiner</title>
<link rel="stylesheet" href="https://fonts.googleapis.com/css2?family=Oswald:wght@300;400;600;700&family=Open+Sans:wght@400;700&display=swap">
<style>
  :root {
    --ink: #1e1e22;
    --cocoa: #46383a;
    --mauve: #5b4a4d;
    --blush: #e2d0c6;
    --blush-light: #e8c9c0;
    --paper: #ffffff;
    --text: #4a4346;
    --muted: #6b6468;
    --sky: #3ea6ef;
    --navy: #3c5a9a;
  }
  * { box-sizing: border-box; margin: 0; padding: 0; }
  html, body { width: 1071px; height: 1200px; overflow: hidden; }
  body { position: relative; background: var(--paper); font-family: "Open Sans", Arial, sans-serif; color: var(--text); }

  .site-header { position: absolute; left: 0; top: 0; width: 1071px; height: 126px; background: var(--ink); }
  .brand { position: absolute; left: 125px; top: 36px; }
  .brand-name { font-family: "Oswald", sans-serif; font-weight: 400; font-size: 31px; line-height: 34px; color: #fff; letter-spacing: 0.2px; }
  .brand-tag { font-family: Arial, sans-serif; font-size: 12.5px; color: var(--blush-light); margin-left: 28px; line-height: 14px; }

  .main-nav { position: absolute; left: 371px; top: 48px; display: flex; }
  .main-nav a { font-family: "Oswald", sans-serif; font-weight: 300; font-size: 17px; color: #fff; text-decoration: none; padding: 0 11px; height: 31px; line-height: 31px; margin-right: 7px; letter-spacing: -0.3px; }
  .main-nav a.is-active { background: var(--blush); color: var(--cocoa); }

  .hero { position: absolute; left: 0; top: 126px; width: 1071px; height: 436px; background: var(--paper); }
  .hero-photo { position: absolute; left: 640px; top: 8px; width: 320px; height: 428px; background: radial-gradient(ellipse at 60% 45%, #d8cec6 0%, #ece7e3 45%, #ffffff 75%); z-index: 0; }
  .hero-title { position: absolute; left: 143px; top: 130px; z-index: 1; font-weight: 700; font-size: 23.5px; line-height: 32px; color: var(--mauve); text-transform: uppercase; white-space: nowrap; }
  .hero-copy { position: absolute; left: 142px; top: 222px; z-index: 1; width: 440px; font-size: 13.6px; line-height: 17.4px; color: var(--text); letter-spacing: -0.4px; }

  .how { position: absolute; left: 0; top: 562px; width: 1071px; height: 309px; background: var(--blush); }
  .how-photo { position: absolute; left: 134px; top: 9px; width: 361px; height: 300px; background: linear-gradient(160deg, #3a3536 0%, #1a1819 55%, #0e0d0e 100%); border-radius: 40px 80px 4px 4px; }
  .how-title { position: absolute; left: 552px; top: 64px; font-family: "Oswald", sans-serif; font-weight: 700; font-size: 62px; line-height: 66px; color: var(--cocoa); letter-spacing: 1px; }
  .how-copy { position: absolute; left: 553px; top: 139px; width: 420px; font-size: 13px; line-height: 15px; color: #2e2628; }
  .btn-more { position: absolute; left: 549px; top: 189px; width: 138px; height: 42px; background: var(--cocoa); color: #fff; font-family: "Oswald", sans-serif; font-weight: 600; font-size: 23px; line-height: 42px; text-align: center; text-decoration: none; letter-spacing: -0.5px; }

  .testimonials { position: absolute; left: 0; top: 871px; width: 1071px; height: 195px; }
  .testimonial { position: absolute; top: 45px; }
  .testimonial-photo { position: absolute; left: 0; top: 0; width: 68px; height: 68px; }
  .testimonial-name { position: absolute; top: 0; font-weight: 400; font-size: 16px; line-height: 19px; color: #3a3336; white-space: nowrap; }
  .testimonial-place { position: absolute; top: 19px; font-family: Arial, sans-serif; font-size: 11px; line-height: 13px; color: var(--muted); white-space: nowrap; }
  .testimonial-quote { position: absolute; top: 39px; width: 186px; font-family: Arial, sans-serif; font-size: 10.8px; line-height: 13px; color: var(--muted); }

  .site-footer { position: absolute; left: 0; top: 1066px; width: 1071px; height: 134px; background: var(--ink); }
  .site-footer .brand { top: 43px; }
  .footer-nav { position: absolute; left: 353px; top: 47px; display: flex; gap: 12px; }
  .footer-nav a { font-family: Arial, sans-serif; font-size: 11px; color: #fff; text-decoration: none; }
  .copyright { position: absolute; left: 353px; top: 69px; font-family: Arial, sans-serif; font-size: 10px; color: #cfcacb; }
  .social { position: absolute; top: 50px; width: 38px; height: 38px; border-radius: 50%; }
  .social-a { left: 847px; background: var(--sky); }
  .social-b { left: 896px; background: var(--navy); }
</style>
</head>
<body>
  <header class="site-header">
    <div class="brand">
      <div class="brand-name">Simon Ashgrove</div>
      <div class="brand-tag">Pianist Teacher Examiner</div>
    </div>
    <nav class="main-nav">
      <a href="#" class="is-active">HOME</a>
      <a href="#">HOW IT WORKS</a>
      <a href="#">ABOUT ME</a>
      <a href="#">STUDENTS TESTIMONIALS</a>
      <a href="#">PRICING</a>
      <a href="#">CONTACT</a>
    </nav>
  </header>

  <section class="hero">
    <div class="hero-photo" role="img" aria-label="Photo of the pianist seated on a black bench, reaching toward a small white toy piano"></div>
    <h1 class="hero-title">Professional classical pianist<br>and a piano teacher of all levels</h1>
    <p class="hero-copy">Dolor nunc vule putateulr ips dol consec.Donec semp ertet laciniate ultricie upien disse comete dolo lectus fgilla itollicil tua ludin dolor. nec met quam accumsan dolore con dime netus lullam utlacus adipiscing ipsum molestie euismod.</p>
  </section>

  <section class="how">
    <div class="how-photo" role="img" aria-label="Photo of a black grand piano with its lid open"></div>
    <h2 class="how-title">HOW IT WORKS</h2>
    <p class="how-copy">Dolor nunc vule putateulr ips dol consec. Donec semp ertet laciniate ultricie upien disse comete. dolo lectus fgilla itollicil tua ludin dolor.</p>
    <a href="#" class="btn-more">MORE INFO</a>
  </section>

  <section class="testimonials">
    <article class="testimonial" style="left:99px">
      <div class="testimonial-photo" role="img" aria-label="Portrait of student Martin Hale at the piano" style="background:linear-gradient(135deg,#6a6462,#2a2627)"></div>
      <h3 class="testimonial-name" style="left:84px">Martin Hale</h3>
      <div class="testimonial-place" style="left:84px">San Francisco</div>
      <p class="testimonial-quote" style="left:85px">Sed ut perspiciatis, unde omnis iste natus error sit voluptatem accusantium doloremque laudantium, totam rem aperiam eaque ipsa, quae ab illo inventore.</p>
    </article>
    <article class="testimonial" style="left:390px">
      <div class="testimonial-photo" role="img" aria-label="Portrait of student Clara Wendt" style="background:linear-gradient(135deg,#8a5a3c,#2e1e16)"></div>
      <h3 class="testimonial-name" style="left:84px">Clara Wendt</h3>
      <div class="testimonial-place" style="left:84px">Australia</div>
      <p class="testimonial-quote" style="left:84px">At vero eos et accusamus et iusto odio dignissimos ducimus, qui blanditiis praesentium voluptatum deleniti atque corrupti, quos dolores et quas molestias excepturi sint, obcaecati.</p>
    </article>
    <article class="testimonial" style="left:680px">
      <div class="testimonial-photo" role="img" aria-label="Portrait of young student Mei Lin Tao at the piano" style="background:linear-gradient(135deg,#7a4a32,#e8ddd6)"></div>
      <h3 class="testimonial-name" style="left:82px">Mei Lin Tao</h3>
      <div class="testimonial-place" style="left:82px">China</div>
      <p class="testimonial-quote" style="left:84px;width:192px">Temporibus autem quibusdam et aut officiis debitis aut rerum necessitatibus saepe eveniet, ut et voluptates repudiandae sint et molestiae no debitis aut rerum necessitatibus.</p>
    </article>
  </section>

  <footer class="site-footer">
    <div class="brand">
      <div class="brand-name">Simon Ashgrove</div>
      <div class="brand-tag">Pianist Teacher Examiner</div>
    </div>
    <nav class="footer-nav">
      <a href="#">Home</a>
      <a href="#">How it works</a>
      <a href="#">About me</a>
      <a href="#">Testimonials</a>
      <a href="#">Pricing</a>
      <a href="#">Contact</a>
    </nav>
    <p class="copyright">© Copyright 2014. Simon Ashgrove. All Rights Reserved.</p>
    <a href="#" class="social social-a" aria-label="Social profile"></a>
    <a href="#" class="social social-b" aria-label="Social page"></a>
  </footer>
</body>
</html>
```